Stationary Set Rebrand for Brenvik

We are a Canadian Distribution and Service Company that was established in 1969. Over the past 5 decades we have expanded our business and have warehouses across Canada. We specialize in adhesive tapes, adhesives, films, safety, warehouse, shipping, janitorial and packaging supplies.

We have updated our logo design and would like a new corporate branding identity that includes a new fresh Stationary Set (Business Cards, Letterhead, Letterhead MS Word, Envelope, Presentation Folders, Email Signatures, Notepad Covers, etc.)

Target Market(s)

Industrial Business Sector

Font styles to use
Sans Serif

Colors
0054AA
0677BA
7BADD7
CADEEF
E8F1F8
0094D4
00A9DD
6FCCEA
C7EBF8
E9F6FB
00AB8E
00BBA5
67D7C9
C6EFE9
E9F9F6
EB3D1F
EC4F4E
F09395
F8D3D4
FCEDEE

Requirements
Should not have
• Colors not too light, darker colours preferred

```html
<!DOCTYPE html>
<html lang="en">
<head>
<meta charset="utf-8">
<title>Brenvik Business Card</title>
<link href="https://fonts.googleapis.com/css2?family=Nunito:wght@400;600&display=swap" rel="stylesheet">
<style>
  :root {
    --stage: #9b9b9b;
    --card: #1b1b1b;
    --card-deep: #0e0e0e;
    --edge: #c8161d;
    --accent: #e0262f;
    --ink-light: #f2f2f2;
    --leaf-light: #5a5a5a;
  }
  * { margin: 0; padding: 0; box-sizing: border-box; }
  html, body {
    width: 1200px; height: 1083px; overflow: hidden;
    background: var(--stage);
    font-family: "Nunito", sans-serif;
  }
  .canvas {
    position: relative; width: 1200px; height: 1083px;
    display: flex; flex-direction: column; align-items: center; justify-content: center; gap: 60px;
  }
  .card {
    position: relative; width: 640px; height: 366px;
    background: var(--card);
    border-bottom: 5px solid var(--edge);
    box-shadow: 0 14px 30px rgba(0,0,0,0.3);
  }
  .brand {
    position: absolute; left: 48px; top: 46px;
    display: flex; align-items: center; gap: 12px;
  }
  .brand-name {
    color: var(--ink-light); font-size: 50px; font-weight: 600; letter-spacing: 1px; line-height: 1;
  }
  .brand-mark { width: 14px; height: 14px; background: var(--accent); }
  .contact {
    position: absolute; left: 48px; top: 178px;
    color: var(--ink-light); font-size: 16px; line-height: 1.35;
  }
  .contact-address { margin-bottom: 12px; }
  .contact-list { list-style: none; }
  .contact-list li { display: flex; align-items: center; gap: 10px; }
  .contact-list svg { width: 13px; height: 13px; flex: none; }
  .person {
    position: absolute; left: 388px; top: 206px;
    padding-left: 16px; border-left: 1.5px solid var(--accent);
  }
  .person-name {
    color: var(--accent); font-size: 20px; font-weight: 600; letter-spacing: 1px; text-transform: uppercase; line-height: 1.2;
  }
  .person-title { color: var(--ink-light); font-size: 15px; line-height: 1.4; }
  .card-back { overflow: hidden; }
  .leaf-pattern {
    position: absolute; inset: 0;
    background: linear-gradient(120deg, var(--leaf-light) 0%, #2c2c2c 45%, var(--card-deep) 75%);
  }
</style>
</head>
<body>
<main class="canvas">
  <section class="card card-front">
    <div class="brand">
      <span class="brand-name">Brenvik</span>
      <span class="brand-mark"></span>
    </div>
    <div class="contact">
      <p class="contact-address">412 Harbour Road<br>Suite 210, Halton, ON 48213</p>
      <ul class="contact-list">
        <li>
          <svg viewBox="0 0 16 16"><path fill="var(--accent)" d="M3.6 1.5l2.3 2.8-1.4 1.6c.9 2 2.6 3.7 4.6 4.6l1.6-1.4 2.8 2.3-1.5 2.6C6.8 13.5 2.5 9.2 1 3z"/></svg>
          <span>555-214-7730</span>
        </li>
        <li>
          <svg viewBox="0 0 16 16"><rect x="1" y="3" width="14" height="10" fill="var(--accent)"/><path d="M1 3l7 6 7-6" fill="none" stroke="var(--card)" stroke-width="1.3"/></svg>
          <span>martin.caldwell@brenvikpack.com</span>
        </li>
        <li>
          <svg viewBox="0 0 16 16" fill="none" stroke="var(--accent)" stroke-width="1.2"><circle cx="8" cy="8" r="6.5"/><ellipse cx="8" cy="8" rx="3" ry="6.5"/><path d="M1.5 8h13M2.5 4.8h11M2.5 11.2h11"/></svg>
          <span>brenvikpack.com</span>
        </li>
      </ul>
    </div>
    <div class="person">
      <p class="person-name">Martin Caldwell</p>
      <p class="person-title">Development Manager Officer</p>
    </div>
  </section>

  <section class="card card-back">
    <div class="leaf-pattern" role="img" aria-label="Repeating pattern of glossy brand leaf symbols in fading greys on black, one highlighted in red"></div>
  </section>
</main>
</body>
</html>
```